Chamber of Commerce Web Design Project

We are working with Marigold Chamber of Commerce. They are a new chamber of commerce forming in SoCal.
Some sites to use for inspiration:
https://brevenlochamber.org
https://varnidel.org
https://www.quoratlinchamber.com
https://www.wtchamber.com
https://morvendipcc.org
Thank you for taking the time to consider designing a website for us. We are web developers based in Stockton, CA, USA. Most of our projects go through the same process. Understanding this process may help you win a project with us. We custom-code all of our websites in-house. We don’t have any requirements as to what tools you use for your design, but we prefer Figma files. For any design that we label as four-stars, we send it to the client for review. The client picks the final design they want us to use. Once we complete this process, we will continue to show additional clients all the four-star sites and purchase them later. Your designs will have multiple chances to sell. For better chances of success, we ask that you follow these guidelines.
IMAGES:
If you use any images or icons in the design, we ask that you have a link to the asset so we can purchase the image/icon. Most of the designs we submit do not have the customer’s images on them unless they have some great images. Be creative; show us the feeling you are trying to portray with your image choices. Use any royalty-free site you choose. We subscribe to Adobe and mainly use their images, but we can purchase images outside of Adobe.
PLEASE NOTE: we will not submit designs to clients with watermarks on the images.
FONTS:
We ask that you identify the fonts used in the design. This can be done in a message if you want. We typically use Google Fonts and Adobe Fonts.
CONTENT:
We're always open to different content and ideas. We often submit designs with stock images so the client can see our vision. We typically take pictures after the website launch to use their images with our vision. Lorem Ipsum is fine for paragraphs, but we ask that you write the headers in correct English. We want to be able to show the vision and identify the sections of the website.
INSPIRATION:
We typically add a couple of links in the brief of websites we like to help you get started in your design.
REVISIONS:
We do not often ask for revisions of the designs unless we see something in the design that may not appeal to the client. If there are slight changes that we want to make, we do that in the development process.
FEEDBACK:
We rarely give feedback on designs during the design process. We are working on many website projects and do not have the time to provide feedback. We usually respond if your request is well thought out and asks specific questions, but a note asking “feedback, please” usually goes unanswered.

```html
<!DOCTYPE html>
<html lang="en">
<head>
<meta charset="utf-8">
<title>Marigold Chamber of Commerce</title>
<link rel="stylesheet" href="https://fonts.googleapis.com/css2?family=Montserrat:wght@400;500;600;700&display=swap">
<style>
:root{
  --blue:#0578c6;
  --bright:#1e8ef0;
  --navy:#0b3d63;
  --dark:#143650;
  --ink:#2b3340;
  --grey:#6b7280;
  --light:#f1f4f8;
  --sky:#8fd0fb;
  --orange:#f2a31c;
  --teal:#0d6b9c;
  --stage:#e1dfe0;
}
*{margin:0;padding:0;box-sizing:border-box}
html,body{width:1200px;height:1200px;overflow:hidden;background:var(--stage);font-family:"Montserrat",sans-serif;color:var(--ink)}
.page{position:absolute;left:387px;top:38px;width:684px;height:1808px;background:#fff;transform:scale(.621);transform-origin:0 0}
.abs{position:absolute}
.brand{display:flex;align-items:center;gap:5px;font-weight:700;color:var(--blue)}
.brand .dot{width:16px;height:16px;border-radius:50%;background:var(--blue)}
.nav{left:195px;top:24px;display:flex;gap:11px;font-size:7px;color:var(--grey)}
.nav .on{color:var(--bright)}
.btn{display:flex;align-items:center;justify-content:center}
.hero{left:0;top:42px;width:684px;height:221px;background:linear-gradient(180deg,#3a5068 0%,#1d2f44 55%,#10202f 100%)}
.hero-title{right:114px;top:56px;text-align:right;font-weight:700;font-size:33px;line-height:36px;letter-spacing:2px;color:#fff}
.hero-title span{color:var(--bright)}
.arrow{width:28px;height:26px;background:#fff;border-radius:50%;top:140px;font-size:12px;color:#555}
.band{left:0;width:684px;background:var(--blue);color:#fff}
.card-img{top:351px;width:142px;height:80px;background:linear-gradient(135deg,#c9d3dc,#6b7a88)}
.card-lbl{background:#fff;text-align:center;font-size:8px;color:var(--navy);box-shadow:0 1px 3px rgba(0,0,0,.15)}
.card-lbl small{display:block;font-size:6px;color:var(--bright)}
.center{text-align:center}
.para{font-size:8.6px;line-height:12px;color:var(--grey);text-align:center}
.ring{width:76px;height:76px;border:1px dashed #333;border-radius:50%;top:598px}
.ring i{position:absolute;left:7px;top:7px;width:60px;height:60px;border-radius:50%;background:var(--blue)}
.ring svg{position:absolute;left:18px;top:18px}
.prog{font-size:8.5px;color:var(--navy);text-align:center;width:110px;top:682px;line-height:10px}
.logo-box{top:900px;width:104px;height:40px;border:1px solid #777;font-size:12px;line-height:12px;text-align:center;display:flex;align-items:center;justify-content:center;color:#444}
.stat{top:1122px;width:86px;height:42px;color:#fff;text-align:center;font-size:5px;padding-top:10px}
.stat b{display:block;font-size:5.5px;border-bottom:1px dashed rgba(255,255,255,.5);margin:0 8px 5px;padding-bottom:4px}
.post{background:var(--light)}
.post .pic{height:56px;background:linear-gradient(135deg,#3e6e8c,#d97a2a)}
.post p{font-size:8px;line-height:12.5px;color:#444;padding:2px 6px 0}
.post .date{font-size:6px;color:#aaa;padding:0 6px}
.foot h4{font-size:9px;font-weight:600;color:#111;margin-bottom:16px}
.foot a{display:block;font-size:6px;color:#333;text-decoration:none;margin-bottom:10px}
.soc{width:23px;height:23px;border:1px solid var(--blue);border-radius:50%;top:1736px}
</style>
</head>
<body>
<main class="page">
  <!-- header -->
  <div class="abs brand" style="left:43px;top:11px;font-size:10px;line-height:11px"><span class="dot"></span>Marigold Chamber<br>of Commerce</div>
  <div class="abs" style="left:304px;top:8px;font-size:4px;display:flex;gap:3px;align-items:center">Follow Us:
    <span style="width:9px;height:9px;border:1px solid var(--blue);border-radius:50%"></span><span style="width:9px;height:9px;border:1px solid var(--blue);border-radius:50%"></span><span style="width:9px;height:9px;border:1px solid var(--blue);border-radius:50%"></span><span style="width:9px;height:9px;border:1px solid var(--blue);border-radius:50%"></span></div>
  <div class="abs" style="left:140px;top:19px;width:400px;border-top:1px solid #e3e6ea"></div>
  <nav class="abs nav"><span class="on">Home ▾</span><span>About Us ▾</span><span>Membership ▾</span><span>Events ▾</span><span>News ▾</span><span>Contact Us</span></nav>
  <div class="abs" style="left:544px;top:17px;font-size:7px;color:var(--bright);font-weight:600">Log in</div>
  <div class="abs btn" style="left:570px;top:11px;width:71px;height:20px;background:var(--bright);color:#fff;font-size:6px">Become a Member</div>
  <svg class="abs" style="left:648px;top:17px" width="9" height="9" viewBox="0 0 9 9"><circle cx="4" cy="4" r="3" fill="none" stroke="#aab" /><path d="M6 6l2.5 2.5" stroke="#aab"/></svg>

  <!-- hero -->
  <div class="abs hero" role="img" aria-label="Night city skyline seen across the water beside a long pier"></div>
  <div class="abs btn arrow" style="left:0">‹</div>
  <div class="abs btn arrow" style="left:656px">›</div>
  <h1 class="abs hero-title"><span>MARIGOLD</span><br>CHAMBER OF<br>COMMERCE</h1>
  <div class="abs btn" style="left:490px;top:211px;width:79px;height:23px;border:1.5px solid #fff;color:#fff;font-size:8px;letter-spacing:.5px">Join Now</div>

  <!-- mission -->
  <div class="abs band" style="top:263px;height:130px"></div>
  <div class="abs" style="left:107px;top:282px;font-size:7px;color:#ffcf4a">Our Mission</div>
  <div class="abs" style="left:107px;top:292px;width:225px;font-size:8.5px;line-height:13px;font-weight:700;color:#fff">Lorem ipsum dolor sit amet, consectetuer adipiscing elit, sed diam nonummy nibh</div>
  <div class="abs" style="left:356px;top:288px;width:213px;font-size:5.8px;line-height:9px;color:#e6f1fa">Lorem ipsum dolor sit amet, consectetuer adipiscing elit, sed diam nonummy nibh euismod tincidunt ut laoreet dolore magna aliquam erat volutpat. Ut wisi enim ad minim veniam, quis nostrud exerci tation ullamcor</div>

  <div class="abs card-img" style="left:107px" role="img" aria-label="Team of smiling business professionals"></div>
  <div class="abs card-img" style="left:268px;background:linear-gradient(180deg,#2c4a8c,#0d1a3c)" role="img" aria-label="Audience at a conference event"></div>
  <div class="abs card-img" style="left:427px" role="img" aria-label="Three businessmen in suits"></div>
  <div class="abs card-lbl" style="left:121px;top:401px;width:114px;height:41px;background:var(--sky);color:#fff;padding-top:12px;font-size:8px">Who We Are<small style="color:var(--navy);font-size:5px;margin-top:2px">Learn More ⟶</small></div>
  <div class="abs card-lbl" style="left:284px;top:403px;width:112px;height:37px;padding-top:10px"><small>Our Event</small>Featured Event</div>
  <div class="abs card-lbl" style="left:441px;top:403px;width:114px;height:37px;padding-top:10px"><small>Become a member</small>Membership</div>

  <!-- program -->
  <h2 class="abs center" style="left:0;width:684px;top:462px;font-size:13px;font-weight:600;color:#444">Our <span style="color:var(--blue)">Program</span></h2>
  <p class="abs para" style="left:140px;width:404px;top:486px">Lorem ipsum dolor sit amet, consectetuer adipiscing elit, sed diam nonummy nibh euismod tincidunt ut laoreet dolore magna aliquam erat volutpat. Ut wisi enim ad minim veniam, quis nostrud exerci tation ullamcorper suscipit lobortis nisl ut aliquip ex ea commodo consequat.</p>
  <p class="abs para" style="left:136px;width:412px;top:547px">Duis autem vel eum iriure dolor in hendrerit in vulputate velit esse molestie consequat, vel illum dolore eu feugiat nulla facilisis at vero eros et accumsan et iusto odio dignissim qui blandit praesent luptatum zzril delenit augue</p>

  <div class="abs ring" style="left:149px"><i></i><svg width="40" height="40" viewBox="0 0 40 40" fill="none" stroke="#fff" stroke-width="2"><circle cx="20" cy="11" r="6"/><circle cx="11" cy="27" r="6"/><circle cx="29" cy="27" r="6"/></svg></div>
  <div class="abs ring" style="left:255px"><i></i><svg width="40" height="40" viewBox="0 0 40 40" fill="none" stroke="#fff" stroke-width="2.5"><path d="M6 34v-6M13 34v-10M20 34v-14M27 34v-18M34 34v-22"/><path d="M6 20L30 6M24 6h6v6"/></svg></div>
  <div class="abs ring" style="left:363px"><i></i><svg width="40" height="40" viewBox="0 0 40 40" fill="none" stroke="#fff" stroke-width="3"><circle cx="20" cy="20" r="15" fill="#fff"/><path d="M13 20l5 5 9-10" stroke="var(--blue)"/></svg></div>
  <div class="abs ring" style="left:465px"><i></i><svg width="40" height="40" viewBox="0 0 40 40" fill="none" stroke="#fff" stroke-width="2"><path d="M14 20a6 6 0 1 1 12 0c0 3-3 4-3 7h-6c0-3-3-4-3-7zM17 31h6M20 6v4M8 12l3 2M32 12l-3 2"/></svg></div>
  <div class="abs prog" style="left:132px;top:686px">Business Networking</div>
  <div class="abs prog" style="left:238px;top:686px">Career Development</div>
  <div class="abs prog" style="left:346px">Industry Advocacy</div>
  <div class="abs prog" style="left:448px">Conferences and Seminars</div>
  <div class="abs btn" style="left:289px;top:712px;width:108px;height:22px;border-radius:11px;background:var(--blue);color:#fff;font-size:7px">View All Program</div>

  <!-- network band -->
  <div class="abs band" style="top:746px;height:140px"></div>
  <h3 class="abs" style="left:107px;top:760px;width:255px;font-size:10px;line-height:13.5px;font-weight:700;color:#fff">Building a Strong Business Network through Marigold Chamber of Commerce</h3>
  <p class="abs" style="left:107px;top:796px;width:240px;font-size:8px;line-height:12px;color:#0a2a44">Building a strong business network through Marigold Chamber of Commerce, connecting you with professionals and businesses in the pipeline industry.</p>
  <div class="abs btn" style="left:108px;top:836px;width:96px;height:22px;border:1.5px solid #fff;color:#fff;font-size:7px">Become a Member</div>
  <div class="abs" style="left:107px;top:864px;font-size:4px;color:#5da6dc">Join today and grow your business with local partners</div>
  <div class="abs" style="left:361px;top:746px;width:208px;height:140px;background:linear-gradient(135deg,#b7c3cc,#4d5a64)" role="img" aria-label="Business team meeting around a conference table"></div>
  <svg class="abs" style="left:445px;top:802px" width="40" height="40" viewBox="0 0 40 40"><circle cx="20" cy="20" r="18" fill="#f49a1c" stroke="#fff" stroke-width="2"/><path d="M15 11l13 9-13 9z" fill="#fff"/></svg>

  <!-- investors -->
  <div class="abs logo-box" style="left:108px">Logo<br>Investors</div>
  <div class="abs logo-box" style="left:226px">Logo<br>Investors</div>
  <div class="abs logo-box" style="left:345px">Logo<br>Investors</div>
  <div class="abs logo-box" style="left:462px">Logo<br>Investors</div>
  <div class="abs center" style="left:0;width:684px;top:948px;font-size:10px;color:var(--blue);letter-spacing:1px">•••</div>

  <!-- success -->
  <div class="abs" style="left:0;top:964px;width:686px;height:213px;background:linear-gradient(90deg,#2b3f50,#1e3a52 16%,#153a58 16%,#123a5c 83%,#2d4050 83%)" role="img" aria-label="Industrial pipeline facility in blue tones"></div>
  <h3 class="abs" style="left:113px;top:1012px;width:180px;font-size:13px;line-height:16.5px;font-weight:700;color:#fff">Achieving Success with <span style="color:var(--bright)">Marigold</span> Chamber of Commerce</h3>
  <div class="abs btn" style="left:112px;top:1067px;width:58px;height:16px;border:1px solid #fff;color:#fff;font-size:5.5px">Join Now</div>
  <div class="abs" style="left:296px;top:986px;width:113px;height:131px;background:linear-gradient(160deg,#7d8a96,#2a3d52)" role="img" aria-label="Portrait of a smiling businessman holding a tablet"></div>
  <div class="abs" style="left:530px;top:978px;font-size:26px;color:#0b2a44;font-weight:700">”</div>
  <p class="abs" style="left:422px;top:1006px;width:148px;font-size:8.4px;line-height:12px;color:#fff">"Membership with Marigold Chamber of Commerce has helped me expand my business network and stay informed about the pipeline industry."</p>
  <div class="abs" style="left:422px;top:1074px;font-size:6px;font-weight:700;color:#fff">Ellis Varno<div style="font-size:4.5px;font-weight:400">CEO, Marigold Inc.</div></div>
  <div class="abs" style="left:422px;top:1100px;font-size:7px;color:var(--orange)">◀ ▶</div>
  <div class="abs stat" style="left:202px;background:var(--orange)"><b>Membership</b>989+ Membership reviews</div>
  <div class="abs stat" style="left:299px;background:var(--teal)"><b>Investment</b>108+ Investors reviews</div>
  <div class="abs stat" style="left:396px;background:var(--teal)"><b>Partners</b>89+ Partners reviews</div>

  <!-- blog -->
  <div class="abs center" style="left:0;width:682px;top:1186px;font-size:8px;color:var(--bright)">Featured Article</div>
  <h2 class="abs center" style="left:0;width:684px;top:1195px;font-size:13px;font-weight:600;color:#555">Latest from Our Blog</h2>
  <div class="abs post" style="left:108px;top:1218px;width:221px;height:237px">
    <div class="pic" style="height:104px" role="img" aria-label="Worker in safety gear at an illuminated pipeline plant"></div>
    <div style="font-size:6px;color:#aaa;padding:5px 16px 0">Jan 8, 2025</div>
    <div style="font-size:9px;line-height:13px;color:#333;padding:5px 16px 0">The Future of the Pipeline Industry: Challenges and Opportunities</div>
    <div style="font-size:5.6px;line-height:8.5px;color:#aaa;padding:6px 16px 0">The Marigold Chamber of Commerce discusses the future of the pipeline industry and how we can address challenges and capitalize on opportunities.</div>
  </div>
  <div class="abs btn" style="left:124px;top:1417px;width:163px;height:24px;background:#fff;border:1px solid #dde;color:var(--blue);font-size:8px">Read More</div>
  <div class="abs post" style="left:340px;top:1218px;width:106px;height:111px"><div class="pic" role="img" aria-label="Pipeline plant at dusk"></div><p>Innovative Technologies in the Pipeline Industry</p><div class="date">Jan 8, 2025</div></div>
  <div class="abs post" style="left:463px;top:1218px;width:106px;height:111px"><div class="pic" role="img" aria-label="Pipeline plant at dusk"></div><p>The Importance of Networking in Pipeline Business</p><div class="date">Jan 8, 2025</div></div>
  <div class="abs post" style="left:340px;top:1344px;width:106px;height:111px"><div class="pic" role="img" aria-label="Worker walking through a pipeline plant"></div><p>Latest Trends in the Pipeline Industry</p><div class="date" style="margin-top:12px">Jan 8, 2025</div></div>
  <div class="abs post" style="left:463px;top:1344px;width:106px;height:111px"><div class="pic" role="img" aria-label="Pipeline plant at dusk"></div><p>Innovative Technologies in the Pipeline Industry</p><div class="date">Jan 8, 2025</div></div>

  <!-- cta -->
  <div class="abs band" style="top:1477px;height:140px"></div>
  <div class="abs btn" style="left:179px;top:1515px;width:329px;height:59px;border-radius:10px;background:var(--dark);color:#fff;font-size:13px;font-weight:600;box-shadow:2px 3px 4px rgba(0,0,0,.35)">Join Now and Unlock Member Benefits</div>

  <!-- footer -->
  <div class="abs brand" style="left:108px;top:1640px;font-size:13px;line-height:15px"><span class="dot" style="width:24px;height:24px"></span>Marigold Chamber<br>of Commerce</div>
  <div class="abs" style="left:107px;top:1688px;width:149px;height:34px;border:1px solid #ccd;font-size:6px;color:#999;padding:14px 3px">Enter email</div>
  <div class="abs btn" style="left:220px;top:1688px;width:36px;height:34px;background:var(--bright);color:#fff;font-size:6px">Send</div>
  <div class="abs soc" style="left:108px"></div><div class="abs soc" style="left:138px"></div><div class="abs soc" style="left:166px"></div><div class="abs soc" style="left:195px"></div>
  <div class="abs foot" style="left:281px;top:1642px"><h4>Company Policy</h4><a>Terms and Conditions</a><a>Privacy Policy</a><a>Cookie Policy</a><a style="font-weight:700">Connect with us!</a><a>support@marigold.example</a></div>
  <div class="abs foot" style="left:405px;top:1642px"><h4>Company</h4><a>Become a Partner (coming 2025)</a><a>Careers</a><a>About Us</a><a>Blog</a></div>
  <div class="abs foot" style="left:524px;top:1642px"><h4>Services</h4><a>Services</a><a>Membership</a><a>Event</a><a>News</a></div>
  <div class="abs" style="left:112px;top:1782px;width:460px;border-top:1px solid #e3e6ea"></div>
  <div class="abs center" style="left:0;width:684px;top:1789px;font-size:5.5px;color:#aaa">@Copyright 2025 Marigold Chamber of Commerce. <span style="color:var(--blue)">All Rights Reserved.</span></div>
</main>
</body>
</html>
```